Seven Banner Campaigns Need Them Now

I want banners created for 7 campaigns.
For each campaign I need these 6 banner sizes created:
Web Banner Sizes (300x250, 728x90, 160x600)
One of each of these sizes, so 3 web banners
Mobile Banner Sizes (300x50, 216x36, 240x240)
campaign 1
Water emergency restoration
http://www.mendwavelocal.example/
http://www.nearbyshopratings.example/Lincoln-Park-MI/TKV-Recovery-60557.html
campaign2
Highway Sparrow Auto Coverage
http://www.nearbyshopratings.example/Houston-TX/HSAC-Shieldline-60581.html
campaign 3
Velora Free Health Insurance quotes
http://www.nearbyshopratings.example/Velora-66185.html
campaign4
Thrifty Shades
www.nearbyshopratings.example/Aberdeen-SD/Thrifty-Shades-of-Aberdeen-Watertown-and-Sisseton-64613.html
campaign5
Rebuild Masters
http://www.nearbyshopratings.example/Bathroom-Remodeling-Contractors-64668.html
Want to focus on the right contractor for all your home project and remodeling needs
campaign 6
Lasik Eye Surgery
http://www.townlistpages.example/m/beverly-hills-ca-lasik/
http://www.clearsightcenter.example/csc-micro/index.html?venid=Search&subid=QRTB&pid=5550172043&gclid=ZXKPqRTWmNbAFYHJTLpd7GKqRs
focus on a free evaluation with a Lasik specialist
campaign 7
QRX
cash for cars.  focus on sell your junker car for fast cash
we will even come pick it up!
http://www.townlistpages.example/m/spokane-wa-cash-for-cars/
Need these done ASAP..more to come!

Industry/Entity Type
Contractor
Requirements
Must have
- Phone call call to action on each banner

```html
<!DOCTYPE html>
<html lang="en">
<head>
<meta charset="utf-8">
<title>Velora Banner Set</title>
<link rel="stylesheet" href="https://fonts.googleapis.com/css2?family=Open+Sans:wght@400;600;700&display=swap">
<style>
  :root {
    --stage-top: #161616;
    --stage-bottom: #4a4a4a;
    --blue-light: #2a8dc0;
    --blue-mid: #1d77a8;
    --blue-deep: #135a86;
    --orange-light: #f7a531;
    --orange-deep: #ea7a10;
    --white: #ffffff;
    --strip: #f1f1f1;
    --ink: #1a1a1a;
    --photo-sky: #9fb8c8;
    --photo-ground: #6d6a5c;
  }
  * { margin: 0; padding: 0; box-sizing: border-box; }
  html, body { width: 1200px; height: 900px; overflow: hidden; }
  body {
    background: linear-gradient(180deg, var(--stage-top) 0%, var(--stage-bottom) 100%);
    font-family: "Open Sans", Arial, sans-serif;
    color: var(--white);
    position: relative;
  }
  .banner { position: absolute; overflow: hidden; }
  .blue-field { background: linear-gradient(180deg, var(--blue-light) 0%, var(--blue-mid) 45%, var(--blue-deep) 100%); }

  .brand { position: absolute; display: flex; align-items: center; }
  .brand-dot { border-radius: 50%; background: var(--orange-deep); flex: none; }
  .brand-name { font-weight: 700; color: var(--white); line-height: 1; }
  .brand-name.dark { color: var(--ink); }

  .call { position: absolute; text-align: center; font-weight: 700; line-height: 1; }
  .phone {
    position: absolute; display: flex; align-items: center; justify-content: center;
    background: linear-gradient(180deg, var(--orange-light), var(--orange-deep));
    font-weight: 600; color: var(--white); white-space: nowrap;
  }
  .headline { position: absolute; font-weight: 600; text-align: center; line-height: 1.2; }
  .strip { position: absolute; left: 0; width: 100%; background: linear-gradient(180deg, var(--white), var(--strip)); color: var(--ink); display: flex; align-items: center; justify-content: flex-end; }

  /* 160x600 skyscraper */
  .sky { left: 109px; top: 129px; width: 187px; height: 703px; }
  .sky .top { position: absolute; left: 0; top: 0; width: 100%; height: 168px; background: linear-gradient(180deg, var(--blue-mid) 0%, var(--blue-light) 55%, var(--white) 80%, var(--strip) 100%); }
  .sky .photo { position: absolute; left: 0; top: 168px; width: 100%; height: 141px; background: linear-gradient(180deg, var(--photo-sky) 0%, #b9c3c6 50%, var(--photo-ground) 100%); }
  .sky .body { position: absolute; left: 0; top: 309px; width: 100%; height: 394px; }
  .sky .brand { left: 14px; top: 46px; }
  .sky .brand-dot { width: 26px; height: 26px; margin-right: 8px; }
  .sky .brand-name { font-size: 38px; }
  .sky .headline { left: 0; width: 100%; top: 20px; font-size: 34px; line-height: 1.27; font-weight: 600; }
  .sky .sub { position: absolute; left: 0; width: 100%; top: 160px; text-align: center; font-size: 23px; line-height: 1.85; }
  .sky .call { left: 0; width: 100%; top: 296px; font-size: 29px; }
  .sky .phone { left: 5px; top: 333px; width: 171px; height: 49px; font-size: 23px; }

  /* 216x36 */
  .mini { left: 720px; top: 184px; width: 253px; height: 42px; }
  .mini .brand { left: 6px; top: 12px; }
  .mini .brand-dot { width: 10px; height: 10px; margin-right: 4px; }
  .mini .brand-name { font-size: 17px; }
  .mini .tag { position: absolute; left: 74px; top: 5px; font-size: 8px; font-weight: 600; line-height: 1.3; text-align: center; width: 76px; }
  .mini .call { left: 162px; width: 86px; top: 4px; font-size: 12px; }
  .mini .phone { left: 156px; top: 20px; width: 88px; height: 18px; font-size: 10.5px; }

  /* 300x50 */
  .slim { left: 670px; top: 271px; width: 352px; height: 59px; }
  .slim .brand { left: 8px; top: 17px; }
  .slim .brand-dot { width: 14px; height: 14px; margin-right: 5px; }
  .slim .brand-name { font-size: 24px; }
  .slim .tag { position: absolute; left: 100px; top: 6px; font-size: 11px; font-weight: 600; line-height: 1.4; text-align: center; width: 98px; }
  .slim .call { left: 228px; width: 112px; top: 6px; font-size: 17px; }
  .slim .phone { left: 217px; top: 27px; width: 124px; height: 26px; font-size: 15px; }

  /* 300x250 */
  .rect { left: 458px; top: 400px; width: 281px; height: 280px; }
  .rect .brand { left: 10px; top: 42px; }
  .rect .brand-dot { width: 22px; height: 22px; margin-right: 7px; }
  .rect .brand-name { font-size: 34px; }
  .rect .headline { left: 158px; width: 116px; top: 24px; font-size: 20px; line-height: 1.45; }
  .rect .strip { top: 128px; height: 35px; padding-right: 10px; font-size: 18px; }
  .rect .call { left: 0; width: 100%; top: 181px; font-size: 30px; }
  .rect .phone { left: 37px; top: 221px; width: 208px; height: 45px; font-size: 25px; }

  /* 240x240 */
  .square { left: 769px; top: 388px; width: 352px; height: 292px; }
  .square .brand { left: 14px; top: 50px; }
  .square .brand-dot { width: 26px; height: 26px; margin-right: 8px; }
  .square .brand-name { font-size: 44px; }
  .square .headline { left: 200px; width: 148px; top: 18px; font-size: 25px; line-height: 1.45; }
  .square .strip { top: 128px; height: 55px; padding-right: 22px; font-size: 22px; }
  .square .call { left: 0; width: 100%; top: 195px; font-size: 32px; }
  .square .phone { left: 73px; top: 237px; width: 207px; height: 46px; font-size: 26px; }

  /* 728x90 */
  .board { left: 313px; top: 727px; width: 853px; height: 105px; }
  .board .brand { left: 18px; top: 32px; }
  .board .brand-dot { width: 28px; height: 28px; margin-right: 9px; }
  .board .brand-name { font-size: 42px; }
  .board .headline { left: 220px; width: 400px; top: 14px; font-size: 30px; line-height: 1.25; font-weight: 600; }
  .board .headline .light { font-weight: 400; }
  .board .call { left: 630px; width: 206px; top: 13px; font-size: 32px; }
  .board .phone { left: 630px; top: 49px; width: 206px; height: 47px; font-size: 27px; }
</style>
</head>
<body>

  <section class="banner sky">
    <div class="top">
      <div class="brand"><span class="brand-dot"></span><span class="brand-name">Velora</span></div>
    </div>
    <div class="photo" role="img" aria-label="Family photo: parents and children sitting in the open back of an SUV by the coast"></div>
    <div class="body blue-field">
      <h2 class="headline">Smart Insurance Choices</h2>
      <p class="sub">You can<br>Actually Afford</p>
      <p class="call">Call Now!</p>
      <p class="phone">(866) 555-0142</p>
    </div>
  </section>

  <section class="banner mini blue-field">
    <div class="brand"><span class="brand-dot"></span><span class="brand-name">Velora</span></div>
    <p class="tag">Smart Insurance Choices You can Actually Afford</p>
    <p class="call">Call Now!</p>
    <p class="phone">(866) 555-0142</p>
  </section>

  <section class="banner slim blue-field">
    <div class="brand"><span class="brand-dot"></span><span class="brand-name">Velora</span></div>
    <p class="tag">Smart Insurance Choices You can Actually Afford</p>
    <p class="call">Call Now!</p>
    <p class="phone">(866) 555-0142</p>
  </section>

  <section class="banner rect blue-field">
    <div class="brand"><span class="brand-dot"></span><span class="brand-name">Velora</span></div>
    <h2 class="headline">Smart Insurance Choices</h2>
    <p class="strip">You can Actually Afford</p>
    <p class="call">Call Now!</p>
    <p class="phone">(866) 555-0142</p>
  </section>

  <section class="banner square blue-field">
    <div class="brand"><span class="brand-dot"></span><span class="brand-name">Velora</span></div>
    <h2 class="headline">Smart Insurance Choices</h2>
    <p class="strip">You can Actually Afford</p>
    <p class="call">Call Now!</p>
    <p class="phone">(866) 555-0142</p>
  </section>

  <section class="banner board blue-field">
    <div class="brand"><span class="brand-dot"></span><span class="brand-name">Velora</span></div>
    <h2 class="headline">Smart Insurance Choices<br><span class="light">You can Actually Afford</span></h2>
    <p class="call">Call Now!</p>
    <p class="phone">(866) 555-0142</p>
  </section>

</body>
</html>
```